We need a banner for this page on our website:
http://www.lukenorvilleinsight.com/pathways-in-australian-erp/

Dimensions of the image should be approximately 1200 × 500

We are a research-based consultancy and this is a banner to subscribe to our paid content (about corporate technology systems).

Would like the final design to incorporate logo (attached files).
Updates

Banner must include the title "Pathways in Australian ERP"

thanks

Target Market(s)

Business professionals within medium to large Australian organisations and technology companies.

Requirements
Nice to have
• a call to action. something like "subscribe now" or similar. Happy to be directed based on designers customer experience perspective.

Could potentially include "Lifetime Membership"

If including a person consider a male and a female - not one or the other.

```html
<!DOCTYPE html>
<html lang="en">
<head>
<meta charset="utf-8">
<title>Pathways in Australian ERP – Luke Norville Insight</title>
<link rel="stylesheet" href="https://fonts.googleapis.com/css2?family=Arimo:wght@400;700&display=swap">
<style>
  :root {
    --sky-light: #9fdcf3;
    --sky-mid: #2aa6de;
    --ocean: #0b5fae;
    --deep-navy: #06306b;
    --glow: #c8f3ff;
    --brand-navy: #1d3f8e;
    --white: #ffffff;
    --hud-cyan: #8fe6ff;
    --button-top: #1b4f9e;
    --button-bottom: #07264f;
    --button-rim: #5fd6ff;
  }
  * { margin: 0; padding: 0; box-sizing: border-box; }
  html, body { width: 1200px; height: 500px; overflow: hidden; background: var(--deep-navy); }
  .banner {
    position: relative;
    width: 1200px;
    height: 500px;
    overflow: hidden;
    font-family: "Arimo", Arial, sans-serif;
    background:
      radial-gradient(circle at 1010px 240px, var(--glow) 0, rgba(120,220,255,0.55) 110px, rgba(40,170,230,0) 260px),
      radial-gradient(ellipse at 120px 40px, var(--sky-light) 0, rgba(120,210,240,0.6) 220px, rgba(40,160,220,0) 520px),
      linear-gradient(160deg, var(--sky-mid) 0%, var(--ocean) 45%, var(--deep-navy) 100%);
  }
  .brand {
    position: absolute;
    left: 40px;
    top: 58px;
    display: flex;
    align-items: center;
    gap: 12px;
  }
  .brand-mark {
    width: 16px;
    height: 16px;
    background: var(--brand-navy);
  }
  .brand-name {
    font-size: 30px;
    font-weight: 700;
    color: var(--brand-navy);
    letter-spacing: 0.5px;
  }
  .hud {
    position: absolute;
    left: 390px;
    top: 140px;
    width: 460px;
    height: 300px;
  }
  .world-region {
    position: absolute;
    left: 400px;
    top: 186px;
    width: 236px;
    height: 74px;
    border-radius: 40px;
    background: radial-gradient(ellipse at center, rgba(170,240,255,0.55), rgba(170,240,255,0));
  }
  .headline {
    position: absolute;
    left: 80px;
    top: 322px;
    font-size: 41px;
    font-weight: 400;
    color: var(--white);
    letter-spacing: 0.2px;
    white-space: nowrap;
  }
  .portrait {
    position: absolute;
    left: 720px;
    top: 88px;
    width: 370px;
    height: 412px;
    border-radius: 170px 170px 0 0;
    background:
      radial-gradient(ellipse at 55% 30%, rgba(240,205,190,0.9) 0, rgba(240,205,190,0) 90px),
      linear-gradient(180deg, rgba(30,40,70,0.85) 0%, rgba(60,70,100,0.6) 45%, rgba(245,248,252,0.95) 75%, #ffffff 100%);
  }
  .cta {
    position: absolute;
    left: 150px;
    top: 446px;
    width: 556px;
    height: 60px;
    border-radius: 26px 26px 0 0;
    border: 2px solid var(--button-rim);
    border-bottom: none;
    background: linear-gradient(180deg, var(--button-top), var(--button-bottom));
    box-shadow: 0 -2px 10px rgba(95,214,255,0.45);
    color: var(--white);
    font-size: 23px;
    font-weight: 700;
    text-align: center;
    padding-top: 10px;
    text-decoration: none;
  }
</style>
</head>
<body>
  <main class="banner">
    <div class="brand">
      <span class="brand-mark"></span>
      <span class="brand-name">Luke Norville Insight</span>
    </div>

    <div class="world-region" role="img" aria-label="Glowing world map graphic"></div>

    <svg class="hud" viewBox="0 0 460 300" aria-hidden="true">
      <g fill="var(--hud-cyan)" opacity="0.75">
        <rect x="75" y="30" width="3" height="12"/><rect x="81" y="26" width="3" height="16"/>
        <rect x="87" y="28" width="3" height="14"/><rect x="93" y="22" width="3" height="20"/>
        <rect x="99" y="27" width="3" height="15"/><rect x="105" y="24" width="3" height="18"/>
        <rect x="111" y="29" width="3" height="13"/><rect x="117" y="21" width="3" height="21"/>
        <rect x="123" y="26" width="3" height="16"/><rect x="129" y="23" width="3" height="19"/>
        <rect x="135" y="27" width="3" height="15"/><rect x="141" y="20" width="3" height="22"/>
        <rect x="147" y="25" width="3" height="17"/><rect x="153" y="22" width="3" height="20"/>
        <rect x="159" y="18" width="3" height="24"/><rect x="165" y="24" width="3" height="18"/>
        <rect x="171" y="20" width="3" height="22"/><rect x="177" y="14" width="3" height="28"/>
        <rect x="183" y="12" width="3" height="30"/>
      </g>
      <g fill="var(--hud-cyan)" opacity="0.85">
        <rect x="258" y="105" width="10" height="25"/>
        <rect x="272" y="88" width="10" height="42"/>
        <rect x="286" y="95" width="10" height="35"/>
        <rect x="300" y="70" width="10" height="60"/>
        <rect x="314" y="64" width="10" height="66"/>
      </g>
      <line x1="255" y1="57" x2="330" y2="57" stroke="var(--hud-cyan)" stroke-width="1.5" opacity="0.7"/>
      <line x1="178" y1="57" x2="240" y2="57" stroke="var(--hud-cyan)" stroke-width="1.5" opacity="0.7"/>
      <line x1="345" y1="57" x2="410" y2="57" stroke="var(--hud-cyan)" stroke-width="1.5" opacity="0.7"/>
      <g fill="none" stroke="var(--hud-cyan)" stroke-width="2" opacity="0.8">
        <circle cx="207" cy="93" r="10"/>
        <circle cx="207" cy="93" r="3" fill="var(--hud-cyan)"/>
      </g>
      <polyline points="350,125 362,112 370,118 380,104 392,108 404,92 420,86"
                fill="none" stroke="var(--hud-cyan)" stroke-width="1.5" opacity="0.75"/>
    </svg>

    <h1 class="headline">Pathways in Australian ERP</h1>

    <div class="portrait" role="img" aria-label="Photo of a smiling businesswoman in a white shirt"></div>

    <a class="cta" href="http://www.lukenorvilleinsight.com/pathways-in-australian-erp/">Subscribe Now for Lifetime Membership</a>
  </main>
</body>
</html>
```